Business Card for a Dental Office

The design should communicate integrity, quality and reliability. We also want the card look elegant, simple, but still stand out, different from the traditional-dental-office business card.

Business

```html
<!DOCTYPE html>
<html lang="en">
<head>
<meta charset="utf-8">
<title>Harwick Dental Centre – Business Cards</title>
<link rel="stylesheet" href="https://fonts.googleapis.com/css2?family=Lato:wght@400;700;900&family=Oswald:wght@600&display=swap">
<style>
  :root {
    --page-bg: #ece8e2;
    --card-white: #ffffff;
    --ink: #111111;
    --gold: #c9a514;
    --yellow-light: #fbf36a;
    --yellow: #f2e21a;
    --yellow-deep: #d9c40c;
    --shadow: rgba(60, 40, 20, 0.22);
  }
  * { box-sizing: border-box; margin: 0; padding: 0; }
  html, body { width: 1200px; height: 900px; overflow: hidden; }
  body {
    background: var(--page-bg);
    font-family: "Lato", Arial, sans-serif;
    color: var(--ink);
    display: flex;
    align-items: center;
    justify-content: center;
    gap: 48px;
  }
  .card {
    position: relative;
    width: 540px;
    height: 309px;
    background: var(--card-white);
    box-shadow: 0 10px 26px var(--shadow);
    overflow: hidden;
  }
  .card__band {
    position: absolute;
    left: 0; right: 0; bottom: 0;
    background: linear-gradient(180deg, var(--yellow-deep) 0%, var(--yellow-light) 30%, var(--yellow) 70%, var(--yellow-deep) 100%);
  }
  .card__rule {
    position: absolute;
    left: 0; right: 0;
    height: 5px;
    background: var(--ink);
  }
  .brand {
    display: flex;
    align-items: center;
    gap: 10px;
  }
  .brand__mark {
    width: 14px; height: 14px;
    background: var(--ink);
    flex: none;
  }
  .brand__name {
    font-family: "Lato", Arial, sans-serif;
    font-weight: 900;
    text-transform: uppercase;
    color: var(--ink);
    letter-spacing: 0.5px;
  }

  /* Appointment card */
  .appointment .card__band { top: 178px; }
  .appointment .card__rule { top: 170px; }
  .appointment__head {
    position: absolute;
    top: 26px; left: 40px;
    display: flex; align-items: center; gap: 18px;
  }
  .appointment .brand__name { font-size: 15px; }
  .appointment__title {
    font-size: 19px;
    font-weight: 700;
    color: var(--gold);
  }
  .appointment__fields {
    position: absolute;
    top: 70px; left: 40px; right: 40px;
    display: grid;
    gap: 12px;
  }
  .field {
    display: flex; align-items: flex-end; gap: 8px;
    font-size: 13px; font-weight: 700;
  }
  .field__label { width: 52px; }
  .field__line {
    flex: 1;
    border-bottom: 2px dotted var(--ink);
    height: 12px;
  }
  .field__unit { font-size: 12px; }
  .appointment__notice {
    position: absolute;
    top: 178px; left: 0; right: 0; bottom: 0;
    display: flex; align-items: center; justify-content: center;
    font-size: 16px; font-weight: 700;
  }

  /* Contact card */
  .contact .card__band { top: 152px; }
  .contact .card__rule { top: 144px; }
  .contact .brand {
    position: absolute;
    top: 56px; left: 0; right: 0;
    justify-content: center;
  }
  .contact .brand__mark { width: 20px; height: 20px; }
  .contact .brand__name {
    font-family: "Oswald", Arial, sans-serif;
    font-weight: 600;
    font-size: 30px;
  }
  .person {
    position: absolute;
    top: 200px; left: 40px;
    width: 250px;
    text-align: right;
  }
  .person__name { font-size: 22px; font-weight: 400; line-height: 1.1; }
  .person__role { font-size: 15px; margin-bottom: 12px; }
  .person__address { font-size: 16px; line-height: 1.35; }
  .contact-list {
    position: absolute;
    top: 178px; left: 318px;
    list-style: none;
    display: grid; gap: 5px;
    font-size: 14px;
  }
  .contact-list li { display: flex; align-items: center; gap: 8px; }
  .contact-list svg { width: 16px; height: 16px; flex: none; }
</style>
</head>
<body>

  <section class="card appointment" aria-label="Appointment card">
    <div class="card__rule"></div>
    <div class="card__band"></div>
    <header class="appointment__head">
      <div class="brand">
        <span class="brand__mark"></span>
        <span class="brand__name">Harwick Dental Centre</span>
      </div>
      <h2 class="appointment__title">Your Next Appointment is</h2>
    </header>
    <div class="appointment__fields">
      <div class="field"><span class="field__label">Name :</span><span class="field__line"></span></div>
      <div class="field"><span class="field__label">Date :</span><span class="field__line"></span></div>
      <div class="field"><span class="field__label">Time :</span><span class="field__line"></span><span class="field__unit">AM</span><span class="field__line"></span><span class="field__unit">PM</span></div>
    </div>
    <p class="appointment__notice">If unable to keep appointment, kindly give 24hrs notice.</p>
  </section>

  <section class="card contact" aria-label="Business card">
    <div class="card__rule"></div>
    <div class="card__band"></div>
    <div class="brand">
      <span class="brand__mark"></span>
      <span class="brand__name">Harwick Dental Centre</span>
    </div>
    <div class="person">
      <p class="person__name">Daniel Reed</p>
      <p class="person__role">Managing Director</p>
      <p class="person__address">1234, Address GoesHere<br>Country, 12345</p>
    </div>
    <ul class="contact-list">
      <li>
        <svg viewBox="0 0 16 16" aria-hidden="true"><rect width="16" height="16" fill="#111"/><path d="M4 5c0-1 1-1.5 4-1.5S12 4 12 5v1H10V5H6v1H4z M5 7h6l1 5H4z" fill="#f2e21a"/></svg>
        123-456-7890
      </li>
      <li>
        <svg viewBox="0 0 16 16" aria-hidden="true"><rect width="16" height="16" fill="#111"/><rect x="4" y="6" width="8" height="6" fill="none" stroke="#f2e21a" stroke-width="1.4"/><rect x="5.5" y="3" width="5" height="3" fill="#f2e21a"/></svg>
        123-456-7890
      </li>
      <li>
        <svg viewBox="0 0 16 16" aria-hidden="true"><rect width="16" height="16" fill="#111"/><rect x="3" y="4.5" width="10" height="7" fill="none" stroke="#f2e21a" stroke-width="1.3"/><path d="M3 4.5l5 4 5-4" fill="none" stroke="#f2e21a" stroke-width="1.3"/></svg>
        info@youremail.com
      </li>
      <li>
        <svg viewBox="0 0 16 16" aria-hidden="true"><rect width="16" height="16" fill="#111"/><path d="M6.5 9.5l3-3 M7.5 5.5l1-1a2 2 0 013 3l-1 1 M8.5 10.5l-1 1a2 2 0 01-3-3l1-1" fill="none" stroke="#f2e21a" stroke-width="1.4" stroke-linecap="round"/></svg>
        www.yourweb.com
      </li>
    </ul>
  </section>

</body>
</html>
```